Business Card Design Project

I am seeking a business card for my life coaching career. I specialize in coaching executives and entrepreneurs. Consciousness plays a key role in my practice.
Updates

I would like to see different fonts -I don't like the way the capital J looks. I only want my name once on the card, on the front. I like everything centered on the front, with a white background, grey and green on the front; and the same grey on the back with bullet points next to each quality; centered. I like a subtle shadow of the mountains behind the text on the back of the card. I don't want the mountains on either side to be too big. Thank you.

Target Market(s)

Middle age business owners/executives

Industry/Entity Type

Business

Contact Information for Business Card

The front design is my name and a mountain logo. I want to have my name prominently shown.

Requirements
Must have
• Front of card:
• My name prominent sized font
• Helping clients lead more fulfilling lives;
• Executive Life Coach
• 415-362-4807
• pkrelt4@mailvane.net
• Back of Card:
• Providing Unparalleled support
• Providing a safe place to grow in self-awareness
• 20+ years entrepreneurial experience
• Trust
• Integrity
Nice to have
• Easy to read font; warm colors reflecting a masculine personality.

```html
<!DOCTYPE html>
<html lang="en">
<head>
<meta charset="utf-8">
<title>Owen Hartley – Business Cards</title>
<link rel="stylesheet" href="https://fonts.googleapis.com/css2?family=Marcellus&family=Alegreya:wght@400&family=Raleway:wght@300&display=swap">
<style>
  :root {
    --canvas-bg: #e9e6e2;
    --card-white: #ffffff;
    --card-grey: #4a4748;
    --brand-green: #5a7237;
    --ink-dark: #3a3a3a;
    --ink-light: #f2f2f2;
    --card-shadow: 0 10px 28px rgba(0, 0, 0, 0.22);
  }
  * { margin: 0; padding: 0; box-sizing: border-box; }
  html, body {
    width: 1200px;
    height: 1000px;
    overflow: hidden;
    background: var(--canvas-bg);
  }
  .canvas {
    position: relative;
    width: 1200px;
    height: 1000px;
  }
  .card {
    position: absolute;
    width: 560px;
    height: 320px;
    box-shadow: var(--card-shadow);
    display: flex;
    flex-direction: column;
    align-items: center;
    justify-content: center;
  }

  /* Back of card */
  .card-back {
    left: 60px;
    top: 150px;
    background: var(--card-grey);
  }
  .qualities {
    list-style: none;
    font-family: "Alegreya", Georgia, serif;
    font-size: 22px;
    line-height: 1.35;
    color: var(--ink-light);
  }
  .qualities li {
    display: flex;
    align-items: center;
    gap: 12px;
  }
  .qualities .bullet-arrow {
    width: 16px;
    height: 10px;
    flex: none;
  }

  /* Front of card */
  .card-front {
    left: 580px;
    top: 530px;
    background: var(--card-white);
    text-align: center;
  }
  .brand {
    display: flex;
    align-items: center;
    gap: 12px;
  }
  .brand-mark {
    width: 16px;
    height: 16px;
    background: var(--brand-green);
  }
  .brand-name {
    font-family: "Marcellus", Georgia, serif;
    font-size: 46px;
    letter-spacing: 1px;
    color: var(--brand-green);
    line-height: 1;
  }
  .role {
    margin-top: 10px;
    font-family: "Alegreya", Georgia, serif;
    font-size: 19px;
    color: var(--ink-dark);
  }
  .tagline {
    margin-top: 2px;
    font-family: "Alegreya", Georgia, serif;
    font-size: 17px;
    color: var(--ink-dark);
  }
  .contact {
    margin-top: 32px;
    font-family: "Raleway", Arial, sans-serif;
    font-weight: 300;
    font-size: 22px;
    color: var(--ink-dark);
  }
</style>
</head>
<body>
<main class="canvas">

  <section class="card card-back" aria-label="Back of business card">
    <ul class="qualities">
      <li><svg class="bullet-arrow" viewBox="0 0 16 10" aria-hidden="true"><path d="M0 5h11M8 1l5 4-5 4" fill="none" stroke="#f2f2f2" stroke-width="1.8"/></svg>Providing Unparalleled support</li>
      <li><svg class="bullet-arrow" viewBox="0 0 16 10" aria-hidden="true"><path d="M0 5h11M8 1l5 4-5 4" fill="none" stroke="#f2f2f2" stroke-width="1.8"/></svg>Providing a safe place to grow in self-awareness</li>
      <li><svg class="bullet-arrow" viewBox="0 0 16 10" aria-hidden="true"><path d="M0 5h11M8 1l5 4-5 4" fill="none" stroke="#f2f2f2" stroke-width="1.8"/></svg>20+ years of entrepreneurial experience</li>
      <li><svg class="bullet-arrow" viewBox="0 0 16 10" aria-hidden="true"><path d="M0 5h11M8 1l5 4-5 4" fill="none" stroke="#f2f2f2" stroke-width="1.8"/></svg>Trust</li>
      <li><svg class="bullet-arrow" viewBox="0 0 16 10" aria-hidden="true"><path d="M0 5h11M8 1l5 4-5 4" fill="none" stroke="#f2f2f2" stroke-width="1.8"/></svg>Integrity</li>
    </ul>
  </section>

  <section class="card card-front" aria-label="Front of business card">
    <div class="brand">
      <span class="brand-mark" aria-hidden="true"></span>
      <h1 class="brand-name">OWEN HARTLEY</h1>
    </div>
    <p class="role">Executive Life Coach</p>
    <p class="tagline">Helping clients lead more fulfilling lives</p>
    <p class="contact">415-362-4807 | pkrelt4@mailvane.net</p>
  </section>

</main>
</body>
</html>
```